Friendbook landing page design

We are a Video Production Company and plan to launch our Business Fan Page soon. We are running a competition and need a design done for the related Friendbook landing page.

The landing page should have the following copy:

Win a Web Video Advertisement Worth $4000!
To enter you must:
1. Vote for the web video advertisement that you enjoy the most (check out the Poll Tab)
2. "Like" our Friendbook Fan Page
3. Explain what an ideal web video advertisement would look like for your business (Post this on our wall)
Conditions apply so check out the Poll tab for more information. Competition ends June 30th so get voting!

I have included some previous marketing material for reference only. You do not need to use this as a style a guide
Updates

Target Market(s)

Business owners or marketing managers

Requirements
Must have
• Lofty Crane-media Logo
web address included: www.loftycm.example
An image needs to accompany the copy
Should not have
• text only

```html
<!DOCTYPE html>
<html lang="en">
<head>
<meta charset="utf-8">
<title>Win a Web Video Advertisement – Lofty Crane-media</title>
<link href="https://fonts.googleapis.com/css2?family=Anton&family=Arimo:wght@400;700&display=swap" rel="stylesheet">
<style>
  :root {
    --brand-blue: #1f6fb8;
    --deep-blue: #06234f;
    --hero-glow: #2f8fd8;
    --step-number-bg: #bfe0f4;
    --step-text-bg: #e4f2fb;
    --heading-blue: #1b74c2;
    --accent-orange: #f7941d;
    --ink: #111111;
    --white: #ffffff;
    --footer-top: #ffffff;
    --footer-bottom: #cfd6dc;
    --like-border: #9aa6bd;
  }
  * { box-sizing: border-box; margin: 0; padding: 0; }
  html, body { width: 694px; height: 1200px; overflow: hidden; background: var(--white); }
  body { font-family: "Arimo", Arial, sans-serif; color: var(--ink); }
  .page { position: relative; width: 694px; height: 1200px; }

  .prompt-bar {
    position: absolute; left: 0; top: 0; width: 694px; height: 52px;
    background: linear-gradient(#dcefff, #b7d8f3);
    display: flex; align-items: center; justify-content: center; gap: 10px;
    font-weight: 700; font-size: 27px; color: var(--brand-blue);
  }
  .like-chip {
    display: inline-flex; align-items: center; justify-content: center;
    height: 30px; padding: 0 12px; border: 1px solid var(--like-border); border-radius: 3px;
    background: linear-gradient(#fafbfd, #e3e7ef); color: #3b4a6b; font-size: 17px; font-weight: 700;
  }
  .prompt-arrow { position: absolute; left: 10px; top: 4px; }

  .hero {
    position: absolute; left: 0; top: 52px; width: 694px; height: 423px;
    background: radial-gradient(circle at 45% 40%, var(--hero-glow) 0%, #0d4b8f 35%, var(--deep-blue) 75%);
    overflow: hidden;
  }
  .hero-visual {
    position: absolute; left: 120px; top: 10px; width: 460px; height: 330px; border-radius: 50%;
    background: radial-gradient(circle at 50% 45%, rgba(190,230,255,.55), rgba(60,140,210,.25) 55%, rgba(6,35,79,0) 75%);
  }
  .hero-title {
    position: absolute; left: 0; right: 0; top: 168px;
    font-family: "Anton", Impact, sans-serif; font-size: 68px; line-height: 66px;
    color: var(--white); text-align: center; text-transform: uppercase;
    transform: rotate(-4deg); text-shadow: 0 3px 6px rgba(0,0,0,.6);
  }
  .hero-title .amount { color: var(--accent-orange); }

  .entry-heading {
    position: absolute; left: 0; top: 478px; width: 694px; height: 50px;
    text-align: center; font-size: 34px; font-weight: 700; color: var(--heading-blue); line-height: 50px;
  }

  .step { position: absolute; left: 10px; width: 674px; display: flex; }
  .step-number {
    width: 100px; background: var(--step-number-bg); color: var(--brand-blue);
    font-size: 52px; font-weight: 700; display: flex; align-items: center; justify-content: center;
  }
  .step-text {
    flex: 1; margin-left: 5px; background: var(--step-text-bg); padding: 0 22px;
    display: flex; align-items: center; font-size: 25px; font-weight: 700; color: var(--deep-blue); line-height: 1.3;
  }
  .step-text .like-chip { margin-right: 18px; font-size: 19px; height: 36px; }
  .step-1 { top: 532px; height: 112px; }
  .step-2 { top: 650px; height: 100px; }
  .step-2 .step-text { font-size: 30px; }
  .step-3 { top: 756px; height: 120px; }

  .terms {
    position: absolute; left: 0; top: 888px; width: 694px; text-align: center;
    font-size: 20px; line-height: 28px; color: var(--ink);
  }

  .footer-band {
    position: absolute; left: 0; top: 960px; width: 694px; height: 240px;
    background: linear-gradient(var(--footer-top), var(--footer-bottom));
  }
  .brand {
    position: absolute; left: 18px; top: 50px; width: 230px;
    display: flex; align-items: center; gap: 10px;
    font-size: 30px; font-weight: 700; color: var(--brand-blue); line-height: 1.05;
  }
  .brand-dot { width: 34px; height: 34px; border-radius: 50%; background: var(--brand-blue); flex: none; }
  .web-address {
    position: absolute; left: 276px; top: 40px; width: 400px; height: 100px; border-radius: 14px;
    background: linear-gradient(#3e8fd6, var(--brand-blue));
    display: flex; align-items: center; justify-content: center;
    color: var(--white); font-size: 34px; font-weight: 700;
  }
</style>
</head>
<body>
<main class="page">
  <header class="prompt-bar">
    <svg class="prompt-arrow" width="70" height="70" viewBox="0 0 70 70" aria-hidden="true">
      <path d="M58 64 C20 60 10 40 22 14" fill="none" stroke="#1f6fb8" stroke-width="9" stroke-linecap="round"/>
      <path d="M8 22 L24 2 L36 24 Z" fill="#1f6fb8"/>
    </svg>
    <span>Click on the</span><span class="like-chip">Like</span><span>button above</span>
  </header>

  <section class="hero">
    <div class="hero-visual" role="img" aria-label="Glowing globe built from video screens"></div>
    <h1 class="hero-title">Win a web video<br>advertisement<br>worth <span class="amount">$4000!</span></h1>
  </section>

  <h2 class="entry-heading">To Enter You Must</h2>

  <div class="step step-1">
    <div class="step-number">1</div>
    <div class="step-text">Vote for the web video advertisement that you enjoy the most (check out the Poll Tab)</div>
  </div>
  <div class="step step-2">
    <div class="step-number">2</div>
    <div class="step-text"><span class="like-chip">Like</span>Our Friendbook Fan Page</div>
  </div>
  <div class="step step-3">
    <div class="step-number">3</div>
    <div class="step-text">Explain what an ideal web video advertisement would look like for your business (Post this on our wall)</div>
  </div>

  <p class="terms">Conditions apply so check out the Poll tab for more information.<br>Competition ends June 30th so get voting!</p>

  <footer class="footer-band">
    <div class="brand"><span class="brand-dot"></span><span>Lofty Crane-media</span></div>
    <div class="web-address">www.loftycm.example</div>
  </footer>
</main>
</body>
</html>
```